Business Cards

Simple but professional looking business cards

Name: Rina Tolvardi
Title: Principle Systems Applications Consultant
Email: r@kbrx.net.au
web : www.kbrx.net.au
Phone: +61.8.95203417
Mobile: +61.431862055
Updates

Hi All, Please include the office address Level 4, 200 Quarrington St, Harlow Park, KT, 7312

Industry/Entity Type

Business

```html
<!DOCTYPE html>
<html lang="en">
<head>
<meta charset="utf-8">
<title>KBRX Business Cards – Rina Tolvardi</title>
<link rel="stylesheet" href="https://fonts.googleapis.com/css2?family=Open+Sans:wght@400;600;700&family=Tinos&display=swap">
<style>
  :root {
    --page-bg: #5a5b5c;
    --card-white: #ffffff;
    --silver-light: #eef0f2;
    --silver-mid: #d3d7dc;
    --silver-dark: #b9bec5;
    --brand-blue: #2166f0;
    --brand-blue-light: #3f86f7;
    --brand-blue-dark: #1b4fd0;
    --accent-green: #6ee61f;
    --ink-white: #ffffff;
    --title-blue: #2a5fe0;
  }
  html, body {
    margin: 0;
    padding: 0;
    width: 1200px;
    height: 1200px;
    overflow: hidden;
    background: var(--page-bg);
  }
  .sheet {
    width: 1200px;
    height: 1200px;
    display: flex;
    flex-direction: column;
    align-items: center;
    justify-content: center;
    gap: 70px;
  }
  .card {
    width: 880px;
    height: 503px;
    display: block;
    box-shadow: 0 10px 30px rgba(0,0,0,0.35);
  }
  .holder-name {
    font-family: "Open Sans", sans-serif;
    font-weight: 400;
    font-size: 44px;
    letter-spacing: 4px;
    fill: var(--ink-white);
  }
  .contact-line {
    font-family: "Tinos", serif;
    font-size: 20px;
    letter-spacing: 2.5px;
    fill: var(--ink-white);
  }
  .brand-name {
    font-family: "Open Sans", sans-serif;
    font-weight: 600;
    font-size: 84px;
    fill: var(--title-blue);
  }
  .job-title {
    font-family: "Open Sans", sans-serif;
    font-weight: 700;
    font-size: 25px;
    letter-spacing: 3px;
    fill: var(--title-blue);
  }
</style>
</head>
<body>
<main class="sheet">

  <!-- Back of card: name and contact details -->
  <svg class="card card-back" viewBox="0 0 880 503" role="group" aria-label="Business card back">
    <defs>
      <linearGradient id="silverBack" x1="0" y1="0" x2="1" y2="1">
        <stop offset="0" stop-color="var(--silver-light)"/>
        <stop offset="1" stop-color="var(--silver-dark)"/>
      </linearGradient>
      <linearGradient id="blueBack" x1="0" y1="0" x2="1" y2="1">
        <stop offset="0" stop-color="var(--brand-blue-dark)"/>
        <stop offset="0.55" stop-color="var(--brand-blue-light)"/>
        <stop offset="1" stop-color="var(--brand-blue)"/>
      </linearGradient>
    </defs>
    <rect class="card-base" width="880" height="503" fill="var(--card-white)"/>
    <rect class="silver-field" x="10" y="10" width="860" height="483" fill="url(#silverBack)"/>
    <path class="green-arc" d="M140,10 C230,80 250,300 205,493" fill="none" stroke="var(--accent-green)" stroke-width="9"/>
    <path class="blue-field" d="M175,10 C275,80 320,260 300,493 L870,493 L870,10 Z" fill="url(#blueBack)" stroke="#4a4f57" stroke-width="1.5"/>
    <rect class="name-pill" x="430" y="188" width="438" height="82" rx="22" fill="var(--accent-green)"/>
    <text class="holder-name" x="455" y="245">Rina Tolvardi</text>
    <g class="contact-block">
      <text class="contact-line" x="325" y="330">Ph:+61.8.95203417</text>
      <text class="contact-line" x="325" y="358">Mob:+61.431862055</text>
      <text class="contact-line" x="325" y="386">r@kbrx.net.au</text>
      <text class="contact-line" x="325" y="414">www.kbrx.net.au</text>
      <text class="contact-line" x="325" y="442">Level 4, 200 Quarrington St, Harlow</text>
      <text class="contact-line" x="325" y="470">Park, KT, 7312</text>
    </g>
  </svg>

  <!-- Front of card: company name and job title -->
  <svg class="card card-front" viewBox="0 0 880 503" role="group" aria-label="Business card front">
    <defs>
      <linearGradient id="blueFront" x1="0" y1="0" x2="1" y2="1">
        <stop offset="0" stop-color="var(--brand-blue)"/>
        <stop offset="1" stop-color="var(--brand-blue-light)"/>
      </linearGradient>
      <radialGradient id="silverFront" cx="0.5" cy="0.4" r="0.6">
        <stop offset="0" stop-color="var(--silver-light)"/>
        <stop offset="1" stop-color="var(--silver-mid)"/>
      </radialGradient>
      <clipPath id="frontInner">
        <rect x="10" y="10" width="860" height="483"/>
      </clipPath>
    </defs>
    <rect class="card-base" width="880" height="503" fill="var(--card-white)"/>
    <g clip-path="url(#frontInner)">
      <rect class="blue-field" x="10" y="10" width="860" height="483" fill="url(#blueFront)"/>
      <circle class="silver-disc" cx="560" cy="300" r="345" fill="var(--silver-dark)"/>
      <circle class="silver-disc-inner" cx="560" cy="300" r="325" fill="url(#silverFront)" stroke="var(--accent-green)" stroke-width="9"/>
    </g>
    <g class="brand-mark">
      <circle class="brand-dot" cx="365" cy="260" r="26" fill="var(--title-blue)"/>
      <text class="brand-name" x="410" y="290">KBRX</text>
    </g>
    <text class="job-title" x="545" y="378" text-anchor="middle">Principle Systems</text>
    <text class="job-title" x="545" y="414" text-anchor="middle">Applications Consultant</text>
  </svg>

</main>
</body>
</html>
```